Artificial Intelligence Software Product Microsite

We specialises in Artificial Intelligence (AI) technology for big data analytics and we have a new product to be launched and requires a product microsite for it. Our product is an AI-driven Predictive/Prescriptive Analytics Engine that does the job of a Data Scientist or a group of Data Scientists, highly intelligent and fully automated, where endusers do not require any machine-learning knowledge. We would like to see a design that's simple yet futuristic and provide an impression that it is highly technological advanced. Key messages to deliver are that it is first of its kind in the world, it deploys state-of-the-art technology, a solution that is easy to adopt and integrate into their existing or planned apps. It is in effect a (or a pool of) Virtual Data Scientist(s) at their disposal that will work for them tirelessly 365 days a year and at a small fraction of the cost of a data scientist. Will provide more details, files/images only to shortlisted designers. Expecting something that is simple and straightforward that sufficiently showcase the product/technology.

Deadline will be extended if necessary to facilitate shortlisted designers.
Updates

Reason: To provide designers with more time for submission and amendments. For those who have not submitted your design, pls do so ASAP and also submit your concept first. Pls ensure that you are designing a Product Micro-site and not a corporate website. It's meant to introduce the product only, not the company. Only an enquiry email address is to be included at the bottom. Already said in my earlier public comments, would want something that is scroll-down to view more info rather then having to click to view different pages. This is a pre-requisite as stated both in my project brief and public comments. Thank you for participating and looking forward to see something really good soon.

Target Market(s)

App Developers in the Software Industry or any Enterprise Customers with in-house apps.

Industry/Entity Type

Computer Software

Coding

Coded - Design and coding required

Number of Pages Required

3 page

Font styles to use
Other font styles liked:
• Pls refer to attachments.

Requirements
Must have
• Please refer to the attached document "VandrelAI 1-page Infosheet". Key message to be delivered is as per this document but need to add in additional information on performance comparisons, which is a small section but only ready on 10th Jul. The microsite doesn't have to be strictly 3 pages but can be less or more if necessary but do go along the lines of the modern sites whereby when options are clicked, the page slides down to the specific option selected instead. Prefers some simple animation, especially for the diagram that depicts the high-level architecture of our AI engine, how the process flows between the different components. Make it simple yet futuristic. The key theme or focal point is "Virtual Data Scientist". Would like to see something that's short and straight to the point, with a clean design.
Nice to have
• If you can use suitable images of a (or group of) human data scientist(s) depicting the transformation to a "Virtual Data Scientist" will be great.
Should not have
• This is a software technology to be introduced and as such, must have a design or theme appropriate for the industry. It should not have the kind of generic look-and-feel that other industries uses.

```html
<!DOCTYPE html>
<html lang="en">
<head>
<meta charset="utf-8">
<title>Vandrel AI</title>
<link href="https://fonts.googleapis.com/css2?family=Roboto:wght@300;400;500;700&display=swap" rel="stylesheet">
<style>
:root{
  --red:#e0262b;
  --ink:#222;
  --nav:#666;
  --body:#666;
  --muted:#9a9a9a;
  --band:#f5f5f5;
  --white:#fff;
  --hero-a:#1e8ec6;
  --hero-b:#0d4f7a;
  --hero-c:#061d2a;
  --social-a:#3b5998;
  --social-b:#29b6ee;
}
*{margin:0;padding:0;box-sizing:border-box}
html,body{width:1200px;height:1184px;overflow:hidden;background:var(--white);font-family:'Roboto',Arial,sans-serif;color:var(--ink)}
.page{position:relative;width:1200px;height:1184px}
.site-header{position:absolute;top:0;left:0;width:1200px;height:95px}
.brand{position:absolute;left:99px;top:27px;font-size:36px;font-weight:700;color:var(--ink);letter-spacing:-.5px}
.main-nav{position:absolute;right:100px;top:39px;display:flex;gap:38px;font-size:13.5px;letter-spacing:.3px}
.main-nav a{color:var(--nav);text-decoration:none}
.main-nav a.active{color:var(--red)}
.hero{position:absolute;top:95px;left:0;width:1200px;height:471px;
  background:radial-gradient(circle at 38% 50%, #a9e3ff 0%, #46b1e3 12%, var(--hero-a) 30%, var(--hero-b) 62%, var(--hero-c) 100%)}
.hero-arrow{position:absolute;top:222px;width:20px;height:30px}
.hero-arrow.prev{left:24px}
.hero-arrow.next{right:24px}
.welcome{position:absolute;top:566px;left:0;width:1200px;height:163px;background:var(--band);text-align:center}
.welcome h1{position:absolute;top:29px;width:100%;font-size:27px;font-weight:700;color:var(--red)}
.welcome p{position:absolute;top:68px;left:158px;width:884px;font-size:12.3px;line-height:20.6px;color:var(--body);font-weight:300}
.features{position:absolute;top:790px;left:101px;width:1000px;display:grid;grid-template-columns:350px 350px 300px;row-gap:61px}
.feature h2{display:flex;align-items:center;gap:10px;font-size:21px;font-weight:400;color:var(--ink);height:30px}
.feature svg{width:22px;height:22px;flex:none}
.feature p{margin-top:3px;width:300px;font-size:10.6px;line-height:17.2px;color:var(--muted);font-weight:300}
.site-footer{position:absolute;top:1089px;left:0;width:1200px;height:95px;background:var(--band)}
.footer-nav{position:absolute;left:99px;top:26px;font-size:11px;color:var(--body)}
.footer-nav a{color:var(--body);text-decoration:none}
.footer-nav span{margin:0 7px}
.copyright{position:absolute;left:99px;top:53px;font-size:11px;color:var(--body)}
.social{position:absolute;left:1038px;top:34px;display:flex;gap:11px}
.social span{width:26px;height:26px;border-radius:50%;display:block}
.social .s1{background:var(--social-a)}
.social .s2{background:var(--social-b)}
</style>
</head>
<body>
<div class="page">
  <header class="site-header">
    <div class="brand">VandrelAI</div>
    <nav class="main-nav">
      <a class="active" href="#">HOME</a><a href="#">WHY</a><a href="#">FOR WHOM</a><a href="#">FOR WHAT</a><a href="#">SUPPORT</a>
    </nav>
  </header>

  <section class="hero" role="img" aria-label="Scientist in safety glasses touching a glowing blue holographic data interface">
    <svg class="hero-arrow prev" viewBox="0 0 20 30"><path d="M15 4 5 15l10 11" fill="none" stroke="#fff" stroke-opacity=".7" stroke-width="2"/></svg>
    <svg class="hero-arrow next" viewBox="0 0 20 30"><path d="M5 4l10 11L5 26" fill="none" stroke="#fff" stroke-opacity=".7" stroke-width="2"/></svg>
  </section>

  <section class="welcome">
    <h1>Welcome to Vandrel AI</h1>
    <p>Aliquam erat volutpat. Quisque aliquet ex nec est vestibulum pulvinar. Pellentesque convallis molestie enim sit amet efficitur. Etiam id imperdiet lectus. Vivamus lacus justo, ultrices nec erat in, euismod iaculis mauris. Vivamus eleifend vitae nulla vel malesuada. In ac malesuada lacus, et consectetur ante. Fusce vitae lectus sit amet mi pulvinar maximus. Aenean placerat, nibh vel accumsan aliquet, magna nibh accumsan nibh, ac tempus nunc ipsum ac tellus.</p>
  </section>

  <section class="features">
    <article class="feature">
      <h2><svg viewBox="0 0 24 24"><circle cx="9" cy="13" r="5" fill="none" stroke="#222" stroke-width="3" stroke-dasharray="3 2"/><circle cx="9" cy="13" r="1.5" fill="#222"/><circle cx="18" cy="7" r="3" fill="none" stroke="#222" stroke-width="2.4" stroke-dasharray="2 1.5"/><circle cx="18" cy="17" r="2.5" fill="none" stroke="#222" stroke-width="2"/></svg>Automated</h2>
      <p>Nunc sit amet consequat risus. Curabitur ac elit leo. In eleifend dui tellus, in scelerisque elit porttitor et. Integer eu massa lacinia, lacinia nulla non, volutpat purus vestibulum dolor.</p>
    </article>
    <article class="feature">
      <h2><svg viewBox="0 0 24 24"><path d="M12 3a6 6 0 0 0-3.5 10.9V17h7v-3.1A6 6 0 0 0 12 3z" fill="none" stroke="#222" stroke-width="2"/><path d="M9.5 19.5h5M10.5 22h3" stroke="#222" stroke-width="2"/></svg>Intelligent</h2>
      <p>Nunc sit amet consequat risus. Curabitur ac elit leo. In eleifend dui tellus, in scelerisque elit porttitor et. Integer eu massa lacinia, lacinia nulla non, volutpat purus vestibulum dolor.</p>
    </article>
    <article class="feature">
      <h2><svg viewBox="0 0 24 24"><path d="M5 5l14 14M19 5 5 19" stroke="#222" stroke-width="4" stroke-linecap="round"/></svg>Inquisitive</h2>
      <p>Nunc sit amet consequat risus. Curabitur ac elit leo. In eleifend dui tellus, in scelerisque elit porttitor et. Integer eu massa lacinia, lacinia nulla non, volutpat purus vestibulum dolor.</p>
    </article>
    <article class="feature">
      <h2><svg viewBox="0 0 24 24"><path d="M3 9h5V6a2 2 0 0 1 4 0v3h5v4h2a2 2 0 0 1 0 4h-2v5H3z" fill="#222"/></svg>Easy to Adopt</h2>
      <p>Nunc sit amet consequat risus. Curabitur ac elit leo. In eleifend dui tellus, in scelerisque elit porttitor et. Integer eu massa lacinia, lacinia nulla non, volutpat purus vestibulum dolor.</p>
    </article>
    <article class="feature">
      <h2><svg viewBox="0 0 24 24"><rect x="1.5" y="6" width="21" height="12" rx="1" fill="none" stroke="#222" stroke-width="1.8"/><path d="M4 9.5h16M4 12h16M7 15h10" stroke="#222" stroke-width="1.4" stroke-dasharray="1.5 1"/></svg>Self-learning</h2>
      <p>Nunc sit amet consequat risus. Curabitur ac elit leo. In eleifend dui tellus, in scelerisque elit porttitor et. Integer eu massa lacinia, lacinia nulla non, volutpat purus vestibulum dolor.</p>
    </article>
    <article class="feature">
      <h2><svg viewBox="0 0 24 24"><path d="M4 20l9-9" stroke="#222" stroke-width="3.5" stroke-linecap="round"/><path d="M13 11a5 5 0 0 1 6.5-7.2L16 7.3l.7 2 2 .7 3.5-3.5A5 5 0 0 1 15 13z" fill="#222"/></svg>Customizable</h2>
      <p>Nunc sit amet consequat risus. Curabitur ac elit leo. In eleifend dui tellus, in scelerisque elit porttitor et. Integer eu massa lacinia, lacinia nulla non, volutpat purus vestibulum dolor.</p>
    </article>
  </section>

  <footer class="site-footer">
    <nav class="footer-nav"><a href="#">Home</a><span>|</span><a href="#">Why</a><span>|</span><a href="#">For Whom</a><span>|</span><a href="#">For What</a><span>|</span><a href="#">Support</a></nav>
    <div class="copyright">Copyright &nbsp;©&nbsp; 2015 &nbsp;Vandrel AI. &nbsp;All rights reserved.</div>
    <div class="social"><span class="s1"></span><span class="s2"></span></div>
  </footer>
</div>
</body>
</html>
```